Business Card Design Project

An education/enrichment centre needs a business card for the directors and teachers. Attached is the logo. apart from the logo, the tact line "learning through experience" is needed to be shown in the card

```html
<!DOCTYPE html>
<html lang="en">
<head>
<meta charset="utf-8">
<title>Bright Oak Academy – Business Card</title>
<link rel="stylesheet" href="https://fonts.googleapis.com/css2?family=Cormorant+Garamond:ital,wght@1,500&family=Roboto+Condensed:wght@400;700&display=swap">
<style>
  :root {
    --ink: #3b55a6;
    --ink-soft: rgba(59, 85, 166, 0.55);
    --ink-fade: rgba(59, 85, 166, 0);
    --paper: #ffffff;
    --backdrop: #e9e7e3;
    --card-shadow: rgba(40, 35, 30, 0.18);
  }
  * { box-sizing: border-box; margin: 0; padding: 0; }
  html, body {
    width: 1200px;
    height: 1000px;
    overflow: hidden;
    background: var(--backdrop);
  }
  .canvas {
    position: relative;
    width: 1200px;
    height: 1000px;
  }
  .card {
    position: absolute;
    left: 280px;
    width: 640px;
    height: 366px;
    background: var(--paper);
    box-shadow: 0 6px 22px var(--card-shadow);
    color: var(--ink);
    overflow: hidden;
  }
  .card--front { top: 96px; }
  .card--back { top: 540px; }

  /* Front */
  .tree-art {
    position: absolute;
    left: 36px;
    top: 28px;
    width: 320px;
    height: 310px;
    background: radial-gradient(ellipse 50% 50% at 50% 50%, var(--ink) 0%, var(--ink-soft) 55%, var(--ink-fade) 100%);
  }
  .tagline {
    position: absolute;
    left: 388px;
    top: 112px;
    font-family: "Cormorant Garamond", serif;
    font-style: italic;
    font-weight: 500;
    font-size: 32px;
    line-height: 1.2;
    color: var(--ink);
  }
  .tagline span { display: block; white-space: nowrap; }
  .tagline .line-2 { padding-left: 24px; }
  .tagline .line-3 { padding-left: 46px; }

  /* Back */
  .brand {
    position: absolute;
    left: 44px;
    top: 54px;
    display: flex;
    align-items: center;
    gap: 14px;
  }
  .brand-dot {
    width: 70px;
    height: 70px;
    border-radius: 50%;
    background: var(--ink);
  }
  .brand-name {
    font-family: "Roboto Condensed", sans-serif;
    font-weight: 700;
    font-size: 24px;
    letter-spacing: 1px;
    line-height: 1.1;
    color: var(--ink);
    text-transform: uppercase;
  }
  .contact {
    position: absolute;
    left: 360px;
    top: 52px;
    font-family: "Roboto Condensed", sans-serif;
    color: var(--ink);
  }
  .person-name {
    font-weight: 700;
    font-size: 26px;
    letter-spacing: 0.5px;
    text-transform: uppercase;
  }
  .person-role {
    font-size: 18px;
    margin-top: 2px;
  }
  .contact-list {
    list-style: none;
    margin-top: 26px;
    font-size: 18px;
  }
  .contact-list li {
    display: flex;
    align-items: center;
    gap: 10px;
    margin-bottom: 10px;
  }
  .contact-icon { width: 22px; height: 22px; flex: none; }
  .office {
    margin-top: 22px;
    font-size: 18px;
    line-height: 1.3;
    font-style: normal;
  }
  .office-name {
    font-weight: 700;
    text-transform: uppercase;
  }
</style>
</head>
<body>
<main class="canvas">
  <section class="card card--front">
    <div class="tree-art" role="img" aria-label="Illustration of a leafy blue tree silhouette"></div>
    <p class="tagline">
      <span class="line-1">“Learning</span>
      <span class="line-2">Through</span>
      <span class="line-3">Experience”</span>
    </p>
  </section>

  <section class="card card--back">
    <div class="brand">
      <div class="brand-dot"></div>
      <div class="brand-name">Bright Oak<br>Academy</div>
    </div>

    <div class="contact">
      <h1 class="person-name">Daniel Koh</h1>
      <p class="person-role">Director</p>

      <ul class="contact-list">
        <li>
          <svg class="contact-icon" viewBox="0 0 24 24" aria-hidden="true">
            <circle cx="12" cy="12" r="12" fill="var(--ink)"/>
            <path d="M8.2 6.5c.4-.3 1-.2 1.3.2l1.2 1.9c.2.4.2.9-.2 1.2l-.8.7c.6 1.3 1.6 2.4 2.9 3l.7-.8c.3-.4.8-.4 1.2-.2l1.9 1.2c.4.3.5.9.2 1.3l-.8 1c-.5.6-1.3.8-2 .5-3-1.2-5.3-3.6-6.5-6.5-.3-.7-.1-1.5.5-2z" fill="#fff"/>
          </svg>
          <span>9182 4455</span>
        </li>
        <li>
          <svg class="contact-icon" viewBox="0 0 24 24" aria-hidden="true">
            <circle cx="12" cy="12" r="12" fill="var(--ink)"/>
            <rect x="6" y="8" width="12" height="8.5" rx="1" fill="#fff"/>
            <path d="M6.5 8.6 12 12.8l5.5-4.2" fill="none" stroke="var(--ink)" stroke-width="1.3"/>
          </svg>
          <span>hello@brightoakacademy.sg</span>
        </li>
      </ul>

      <address class="office">
        <span class="office-name">Bright Oak Academy</span><br>
        18 Willow Crest Road<br>
        Singapore 512348
      </address>
    </div>
  </section>
</main>
</body>
</html>
```